Card for modern wood artisan that builds log homes and timber frames.

Design a card with catchy imagery. With a quick list of things I build and services I offer.

I'd like an English side and a french side. I can provide the text.

I am basically a guy that builds log homes and timber frames , but I am very eco friendly oriented.

I use only eco friendly products to limit my carbon footprint.
I want the client to feel as if they are hiring a good smart builder.

I have been building for a while but just starting out to market myself out there , not just work for other companies. Starting
My own thing legitimately.

I am very conscientious, and I take care of the work I do. I am trying to bring a new age, modern feel to an old profession.

Reason: I am not completely satisfied with A model yet, looking for that masculin rustic artistic design that I havent completely found yet. Thank you for your sumbissions.

Target Market(s)

People looking to hire a builder to design and build their projects.
And contractors that want to hire a quality subcontractor for their jobs.

Industry/Entity Type

Construction

Contact Information for Business Card

I want my logo on it, that I had designed here.
And a list of services I provide.

With my phone number, website adress and Email.

Requirements
Must have
• Artful presentation,
• Eco friendly feel
• I love trees.

```html
<!DOCTYPE html>
<html lang="en">
<head>
<meta charset="utf-8">
<title>Cedarline – Business Cards</title>
<link rel="stylesheet" href="https://fonts.googleapis.com/css2?family=Source+Sans+3:wght@400;600;700&family=Oswald:wght@400&display=swap">
<style>
  :root {
    --stage: #232323;
    --card-grey: #e6e5e3;
    --card-white: #ffffff;
    --gold: #d4921a;
    --gold-light: #e3a93a;
    --ink: #161616;
    --text: #1e1e1e;
  }
  * { margin: 0; padding: 0; box-sizing: border-box; }
  html, body { width: 1200px; height: 900px; overflow: hidden; }
  body {
    background: var(--stage);
    position: relative;
    font-family: "Source Sans 3", "Myriad Pro", Arial, sans-serif;
  }
  .card {
    position: absolute;
    top: 170px;
    width: 346px;
    height: 561px;
    box-shadow: 2px 3px 4px rgba(0,0,0,0.55);
    text-align: center;
    color: var(--text);
  }
  .card--english { left: 259px; background: var(--card-grey); }
  .card--french { left: 631px; background: var(--card-white); }

  .tree-art {
    position: absolute;
    left: 90px;
    top: 48px;
    width: 168px;
    height: 268px;
    background: linear-gradient(180deg, var(--gold-light) 0%, var(--gold) 100%);
  }
  .card--french .tree-art { top: 58px; }

  .brand {
    position: absolute;
    left: 0;
    width: 100%;
    top: 164px;
    display: flex;
    flex-direction: column;
    align-items: center;
  }
  .card--french .brand { top: 173px; }
  .brand-row {
    display: flex;
    align-items: center;
    gap: 10px;
  }
  .brand-mark {
    width: 26px;
    height: 26px;
    background: var(--ink);
  }
  .brand-name {
    font-weight: 700;
    font-size: 34px;
    letter-spacing: 1px;
    color: var(--ink);
    line-height: 1;
  }
  .brand-tagline {
    margin-top: 10px;
    font-family: "Oswald", "Arial Narrow", sans-serif;
    font-size: 14px;
    color: var(--ink);
    letter-spacing: 0.3px;
  }

  .person {
    position: absolute;
    left: 0;
    width: 100%;
    top: 371px;
  }
  .person-name {
    font-weight: 600;
    font-size: 21px;
    color: var(--gold);
    line-height: 24px;
    letter-spacing: 0.2px;
  }
  .person-role {
    font-size: 15px;
    line-height: 18px;
  }

  .contact-icons {
    position: absolute;
    left: 0;
    width: 100%;
    top: 438px;
    display: flex;
    justify-content: center;
    gap: 6px;
  }
  .contact-icons svg { width: 14px; height: 14px; fill: var(--gold); }

  .contact-list {
    position: absolute;
    left: 0;
    width: 100%;
    top: 463px;
    list-style: none;
    font-size: 15px;
    line-height: 20.5px;
  }
</style>
</head>
<body>

<article class="card card--english" lang="en">
  <div class="tree-art" role="img" aria-label="Golden wood-grain illustration of an evergreen tree with roots"></div>
  <div class="brand">
    <div class="brand-row">
      <span class="brand-mark"></span>
      <span class="brand-name">CEDARLINE</span>
    </div>
    <span class="brand-tagline">WOOD ARTISAN</span>
  </div>
  <div class="person">
    <p class="person-name">MATHIS DURAND</p>
    <p class="person-role">Managing Director</p>
  </div>
  <div class="contact-icons">
    <svg viewBox="0 0 24 24" aria-label="Phone"><path d="M6.6 10.8a15 15 0 0 0 6.6 6.6l2.2-2.2c.3-.3.7-.4 1-.2 1.1.4 2.3.6 3.6.6.6 0 1 .4 1 1V20c0 .6-.4 1-1 1A17 17 0 0 1 3 4c0-.6.4-1 1-1h3.5c.6 0 1 .4 1 1 0 1.3.2 2.5.6 3.6.1.3 0 .7-.2 1z"/></svg>
    <svg viewBox="0 0 24 24" aria-label="Email"><path d="M2 5h20v14H2z"/><path d="M3 6l9 7 9-7" fill="none" stroke="#fff" stroke-width="1.5"/></svg>
    <svg viewBox="0 0 24 24" aria-label="Website"><circle cx="12" cy="12" r="10"/><path d="M2 12h20M12 2c3 3 3 17 0 20M12 2c-3 3-3 17 0 20" fill="none" stroke="#fff" stroke-width="1.3"/></svg>
  </div>
  <ul class="contact-list">
    <li>555 0142 777</li>
    <li>info@cedarline.com</li>
    <li>www.cedarline.com</li>
  </ul>
</article>

<article class="card card--french" lang="fr">
  <div class="tree-art" role="img" aria-label="Illustration dorée d’un conifère en veinage de bois, avec racines"></div>
  <div class="brand">
    <div class="brand-row">
      <span class="brand-mark"></span>
      <span class="brand-name">CEDARLINE</span>
    </div>
    <span class="brand-tagline">ARTISAN DE BOIS</span>
  </div>
  <div class="person">
    <p class="person-name">MATHIS DURAND</p>
    <p class="person-role">Directeur général</p>
  </div>
  <div class="contact-icons">
    <svg viewBox="0 0 24 24" aria-label="Téléphone"><path d="M6.6 10.8a15 15 0 0 0 6.6 6.6l2.2-2.2c.3-.3.7-.4 1-.2 1.1.4 2.3.6 3.6.6.6 0 1 .4 1 1V20c0 .6-.4 1-1 1A17 17 0 0 1 3 4c0-.6.4-1 1-1h3.5c.6 0 1 .4 1 1 0 1.3.2 2.5.6 3.6.1.3 0 .7-.2 1z"/></svg>
    <svg viewBox="0 0 24 24" aria-label="Courriel"><path d="M2 5h20v14H2z"/><path d="M3 6l9 7 9-7" fill="none" stroke="#fff" stroke-width="1.5"/></svg>
    <svg viewBox="0 0 24 24" aria-label="Site web"><circle cx="12" cy="12" r="10"/><path d="M2 12h20M12 2c3 3 3 17 0 20M12 2c-3 3-3 17 0 20" fill="none" stroke="#fff" stroke-width="1.3"/></svg>
  </div>
  <ul class="contact-list">
    <li>555 0142 777</li>
    <li>info@cedarline.com</li>
    <li>www.cedarline.com</li>
  </ul>
</article>

</body>
</html>
```